construction company business card

I need a business card design for a new company called TK BUILDING PARTNERS. I'd like to see different designs with the name tk BUILDING PARTNERS, and others for TK Building Partners. The company field is Home Improvement and everything related with construction. Colors I like are red, blue and black. The final design should communicate/show simplicity and security.

Industry/Entity Type

Construction

Contact Information for Business Card

TK BUILDING PARTNERS
Tobias Kendrick
(555)046-7293
57-31 213th Avenue
Larkfield Hollow
10982, NY

Requirements
Must have
• HOME IMPROVEMENT

```html
<!DOCTYPE html>
<html lang="en">
<head>
<meta charset="utf-8">
<title>TK Building Partners – Business Card</title>
<link rel="stylesheet" href="https://fonts.googleapis.com/css2?family=Montserrat:wght@400;600;700;800&display=swap">
<style>
  :root {
    --paper: #ffffff;
    --ink: #000000;
    --frame-red: #c8323f;
    --frame-blue: #1aaee6;
    --band-blue: #2b6aab;
    --band-red: #e41f41;
    --text-light: #ffffff;
  }
  html, body {
    margin: 0;
    padding: 0;
    overflow: hidden;
    background: var(--paper);
  }
  .card {
    position: relative;
    width: 1200px;
    height: 703px;
    background: var(--paper);
    overflow: hidden;
    font-family: "Montserrat", Arial, sans-serif;
  }
  .frame {
    position: absolute;
    border-style: solid;
    box-sizing: border-box;
  }
  .frame--outer {
    left: 21px; top: 21px; width: 1157px; height: 420px;
    border-width: 3px 3px 0 3px;
    border-color: var(--frame-red);
  }
  .frame--inner {
    left: 42px; top: 43px; width: 1115px; height: 400px;
    border-width: 3px 3px 0 3px;
    border-color: var(--frame-blue);
  }
  .brand {
    position: absolute;
    left: 44px; top: 46px; width: 1111px; height: 382px;
    display: flex;
    flex-direction: column;
    align-items: center;
    justify-content: center;
    color: var(--ink);
    text-align: center;
  }
  .brand-name {
    margin: 0;
    font-weight: 800;
    font-size: 100px;
    line-height: 1.06;
    letter-spacing: 1px;
  }
  .brand-name span { display: block; }
  .brand-tagline {
    margin: 18px 0 0;
    font-weight: 600;
    font-size: 32px;
    line-height: 1;
    letter-spacing: 8px;
  }
  .band-blue {
    position: absolute;
    left: 0; top: 428px; width: 1200px; height: 25px;
    background: var(--band-blue);
  }
  .band-red {
    position: absolute;
    left: 0; top: 453px; width: 1200px; height: 250px;
    background: var(--band-red);
    color: var(--text-light);
  }
  .contact-name {
    position: absolute;
    left: 110px; top: 22px;
    margin: 0;
    font-weight: 700;
    font-size: 44px;
    line-height: 1;
  }
  .contact-details {
    position: absolute;
    left: 583px; top: 24px;
    margin: 0;
    font-style: normal;
    font-size: 40px;
    line-height: 56px;
  }
  .contact-phone {
    display: block;
    font-weight: 700;
    line-height: 1;
    margin-bottom: 10px;
  }
  .contact-line {
    display: block;
    font-weight: 400;
  }
</style>
</head>
<body>
  <div class="card">
    <div class="frame frame--outer"></div>
    <div class="frame frame--inner"></div>

    <header class="brand">
      <h1 class="brand-name">
        <span>TK BUILDING</span>
        <span>PARTNERS</span>
      </h1>
      <p class="brand-tagline">HOME IMPROVEMENT</p>
    </header>

    <div class="band-blue"></div>
    <div class="band-red">
      <p class="contact-name">Tobias Kendrick</p>
      <address class="contact-details">
        <span class="contact-phone">(555)046-7293</span>
        <span class="contact-line">57-31 213th Avenue</span>
        <span class="contact-line">Larkfield Hollow 10982, NY</span>
      </address>
    </div>
  </div>
</body>
</html>
```